A book cover for an ESL self-study guide to English small talk with exercises and answers

I need a book cover for an ESL self-study guide to English small talk with exercises. It has useful phrases, idioms, and vocabulary in it but I will provide the blub for the back of the book. I would like a simple design. I had the idea to use a red background and the letters 'English' being large across the front in Union Jack lettering then 'ESL' below in different lettering and Small talk further down. I am not sure if the Union Jack lettering will stand out well enough on a red background so we might have to use a different background or edging for those letters but Ideally, I'd like the book to be red and either the 'ESL' or 'Small Talk' to be a vivid blue but again if something else looks better go with it. If it looks like this design idea doesn't work I am open to other ideas too. If the Union Jack lettering is not used I will need a Union Jack on there somewhere to show that the book is in British English. Those are my ideas but ultimately, you guys are the professionals.

Target Market(s)

People who are learning English from ESL students to professionals. I expect the market to be more professionals.

Industry/Entity Type

Education.

Colors
EB3D1F
EC4F4E
F09395
F8D3D4
FCEDEE

Requirements
Must have
• A Union Jack or union jack lettering to show the book is in British English. I would like to cover to be striking and stand out from the others in it's genre without being gaudy.
Nice to have
• I would like the cover to be red but ultimately you guys are the professionals and I'm sure you know more than I do. Scripts should be easy to read as it's for ESL students.

```html
<!DOCTYPE html>
<html lang="en">
<head>
<meta charset="UTF-8">
<title>English Small Talk — Book Cover</title>
<link rel="stylesheet" href="https://fonts.googleapis.com/css2?family=Bebas+Neue&family=Montserrat:wght@800&family=Sacramento&display=swap">
<style>
  :root {
    --backdrop: #0f4190;
    --paper-light: #f2f2f2;
    --paper-dark: #dcdcdc;
    --brand-red: #d9432a;
    --brand-red-deep: #c8321f;
    --navy: #26306b;
    --navy-dark: #1d2456;
    --flag-blue: #1d2a6b;
    --flag-red: #c8321f;
    --flag-white: #ffffff;
  }
  * { margin: 0; padding: 0; box-sizing: border-box; }
  html, body {
    width: 1200px;
    height: 960px;
    overflow: hidden;
    background: var(--backdrop);
  }
  .canvas {
    position: relative;
    width: 1200px;
    height: 960px;
    background: var(--backdrop);
  }
  .cover {
    position: absolute;
    left: 320px;
    top: 70px;
    width: 560px;
    height: 820px;
    background: linear-gradient(120deg, var(--paper-light) 0%, var(--paper-dark) 100%);
    overflow: hidden;
  }
  .stripe-navy {
    position: absolute;
    left: 0; top: 34px;
    width: 100%; height: 10px;
    background: var(--navy-dark);
  }
  .stripe-red {
    position: absolute;
    left: 0; top: 56px;
    width: 100%; height: 32px;
    background: linear-gradient(90deg, var(--brand-red) 0%, var(--brand-red-deep) 100%);
  }
  .title {
    position: absolute;
    left: 0; top: 160px;
    width: 100%;
    text-align: center;
    font-family: "Bebas Neue", "Oswald", sans-serif;
    font-weight: 400;
    font-size: 300px;
    line-height: 0.76;
    letter-spacing: 0;
    color: var(--brand-red);
    transform: scaleX(0.82);
    transform-origin: center top;
  }
  .title span { display: block; }
  .title-script {
    position: absolute;
    left: 0; top: 548px;
    width: 100%;
    text-align: center;
    font-family: "Sacramento", cursive;
    font-size: 120px;
    line-height: 1;
    color: var(--navy);
    transform: rotate(-3deg);
  }
  .rating {
    position: absolute;
    left: 0; top: 712px;
    width: 100%;
    text-align: center;
    font-family: "Montserrat", sans-serif;
    font-size: 15px;
    letter-spacing: 6px;
    color: var(--navy);
  }
  .subtitle {
    position: absolute;
    left: 0; top: 738px;
    width: 100%;
    text-align: center;
    font-family: "Montserrat", sans-serif;
    font-weight: 800;
    font-size: 13px;
    line-height: 1.25;
    letter-spacing: 0.3px;
    text-transform: uppercase;
    color: var(--navy);
  }
  .union-flag {
    position: absolute;
    left: 256px; top: 782px;
    width: 48px; height: 24px;
    display: block;
  }
</style>
</head>
<body>
<div class="canvas">
  <section class="cover">
    <div class="stripe-navy"></div>
    <div class="stripe-red"></div>
    <h1 class="title"><span>Eng</span><span>lish</span></h1>
    <p class="title-script">Small Talk</p>
    <p class="rating">★★★★★</p>
    <p class="subtitle">An ESL self-study guide to<br>English small talk with exercises</p>
    <svg class="union-flag" viewBox="0 0 60 30" role="img" aria-label="Union Jack flag, British English edition">
      <clipPath id="flag-clip"><rect width="60" height="30"/></clipPath>
      <g clip-path="url(#flag-clip)">
        <rect width="60" height="30" fill="var(--flag-blue)"/>
        <path d="M0,0 L60,30 M60,0 L0,30" stroke="var(--flag-white)" stroke-width="6"/>
        <path d="M0,0 L60,30 M60,0 L0,30" stroke="var(--flag-red)" stroke-width="2"/>
        <path d="M30,0 V30 M0,15 H60" stroke="var(--flag-white)" stroke-width="10"/>
        <path d="M30,0 V30 M0,15 H60" stroke="var(--flag-red)" stroke-width="6"/>
      </g>
    </svg>
  </section>
</div>
</body>
</html>
```